Roofing Company Now Hiring and Call Now Facebook Ads

Trying to hire new sales reps in our Alabama market to add to our growing team. This is a great opportunity for any one looking for a career change or looking to add time back to the time they get to spend at home with their families. This is a chance to build a career in one of the fastest growing industries in the country and build financial freedom and a solid future for your family while easily making 6 figures yearly. Sales reps get to set their own schedule, take vacations when they want, and could even choose if they wanted to work in the summer or the winter seasons if they dont like the heat/cold environment. Sales reps are commission based with bonus/incentives for completing task and assignments weekly.

"Let's Talk About Your Roof!" Schedule a free Roof Inspection today!

Needing facebook ads for hiring and a few ads templates for daily post regarding roof inspections and roof replacements, if they are editable it would be easier for me to manage a few templates. This project needs to have a swag/cleanish look that attracts the younger group of people but still make the older group of customer think, man these guys have some solid looking things going on and looks like a well managed and built company. We also target the upper scale areas when seeking customers.

Lets see what yall got! lets Gooo!

Target Market(s)

Property owners, sales reps, homeowners, property managers, job seekers

Industry/Entity Type

Roofing Contractor Storm Restoration Contractor, Construction Contractor

Font styles to use
Sans Serif

Colors
EB3D1F
EC4F4E
F09395
F8D3D4
FCEDEE

Requirements
Must have
• Clean modern professional look with visible red and black colors, we like white too.
Nice to have
• red, black, white, popping eye catching colors.
Should not have
• wrong color red, red is more of a kelvard herons red, please stay away from the pinkish red.

```html
<!DOCTYPE html>
<html lang="en">
<head>
<meta charset="utf-8">
<title>Let's Talk About Your Roof – Summit Crest Roofing</title>
<link href="https://fonts.googleapis.com/css2?family=Alfa+Slab+One&family=Poppins:wght@400;800&display=swap" rel="stylesheet">
<style>
  :root {
    --sky: #d4eef1;
    --sky-deep: #c6e7ea;
    --brand-red: #e0232a;
    --ink: #0b0b0b;
    --dark: #1a1a1a;
    --white: #ffffff;
    --house-light: #e9e4dc;
    --house-mid: #8b7a6a;
    --house-dark: #2a2624;
  }
  * { margin: 0; padding: 0; box-sizing: border-box; }
  html, body {
    width: 1200px;
    height: 1200px;
    overflow: hidden;
    background: var(--sky);
  }
  .ad {
    position: relative;
    width: 1200px;
    height: 1200px;
    background: linear-gradient(180deg, var(--sky) 0%, var(--sky-deep) 100%);
    overflow: hidden;
  }
  .headline {
    position: absolute;
    top: 66px;
    left: 0;
    width: 100%;
    text-align: center;
  }
  .headline-lead {
    font-family: "Poppins", sans-serif;
    font-weight: 400;
    font-size: 40px;
    letter-spacing: 1px;
    color: var(--dark);
    line-height: 1;
  }
  .headline-main {
    font-family: "Alfa Slab One", serif;
    font-size: 128px;
    color: var(--brand-red);
    line-height: 1;
    margin-top: 16px;
    letter-spacing: 2px;
  }
  .house-visual {
    position: absolute;
    left: 17px;
    top: 265px;
    width: 1177px;
    height: 700px;
    border-radius: 6px;
    background:
      linear-gradient(180deg, rgba(42,38,36,0.85) 0%, rgba(42,38,36,0.15) 22%, rgba(0,0,0,0) 40%),
      linear-gradient(90deg, var(--house-light) 0%, #f2eee6 45%, var(--house-mid) 80%, var(--house-dark) 100%);
  }
  .footer-shapes {
    position: absolute;
    left: 0;
    bottom: 0;
    width: 1200px;
    height: 350px;
  }
  .footer-shapes .band-black { fill: var(--ink); }
  .footer-shapes .band-red { fill: var(--brand-red); }
  .brand-name {
    position: absolute;
    left: 98px;
    top: 1030px;
    width: 410px;
    text-align: center;
    font-family: "Poppins", sans-serif;
    font-weight: 800;
    font-size: 46px;
    line-height: 1.1;
    color: var(--white);
    letter-spacing: 1px;
  }
  .cta {
    position: absolute;
    left: 650px;
    top: 1058px;
    width: 480px;
    text-align: center;
    font-family: "Poppins", sans-serif;
    font-weight: 400;
    font-size: 35px;
    line-height: 1.35;
    color: var(--white);
    letter-spacing: 0.5px;
  }
</style>
</head>
<body>
  <main class="ad">
    <header class="headline">
      <p class="headline-lead">"LET'S TALK ABOUT</p>
      <h1 class="headline-main">YOUR ROOF!</h1>
    </header>

    <div class="house-visual" role="img" aria-label="Illustration of a modern two-storey house with white walls, dark metal roofs, large windows, a wooden garage door and trees behind"></div>

    <svg class="footer-shapes" viewBox="0 850 1200 350" preserveAspectRatio="none" aria-hidden="true">
      <path class="band-black" d="M0 895 L660 968 L660 1200 L0 1200 Z"/>
      <path class="band-red" d="M612 962 L1200 855 L1200 1200 L592 1200 Q578 1080 578 1000 Q580 968 612 962 Z"/>
    </svg>

    <p class="brand-name">SUMMIT CREST<br>ROOFING</p>

    <p class="cta">SCHEDULE A FREE ROOF<br>INSPECTION TODAY!</p>
  </main>
</body>
</html>
```